Hi,

I am in desperate need of Wordpress website template for for my consulting company. All the graphics are already there, but I need someone who can code that into an extremely nice template for Wordpress (latest version 3.8.1)

I specialize in Consulting and Advise on global software delivery, with a special focus on how to secure innovation within the global delivery platform. I do have the logo and visual identity.

```html
<!DOCTYPE html>
<html lang="en">
<head>
<meta charset="utf-8">
<title>Novaleap — Global Software Delivery Consulting</title>
<link href="https://fonts.googleapis.com/css2?family=Open+Sans:wght@400;600&family=Ubuntu:wght@300;400&display=swap" rel="stylesheet">
<style>
:root{
  --ink:#333;
  --muted:#666;
  --soft:#8a8a8a;
  --brand:#1e6485;
  --brand-dark:#1a4f78;
  --band-top:#3b8aa9;
  --band-bottom:#1b5582;
  --footer:#f2f2f2;
  --white:#fff;
}
*{margin:0;padding:0;box-sizing:border-box}
html,body{width:765px;height:1200px;overflow:hidden;background:var(--white)}
body{position:relative;font-family:"Open Sans",sans-serif;color:var(--ink)}
.abs{position:absolute}
.heading{font-family:"Ubuntu",sans-serif;font-weight:300}

/* header */
.site-header{left:0;top:0;width:765px;height:88px}
.brand{left:56px;top:18px;display:flex;align-items:center;gap:10px}
.brand-dot{width:52px;height:52px;border-radius:50%;background:var(--brand)}
.brand-name{font-family:"Open Sans",sans-serif;font-weight:600;font-size:17px;color:var(--brand);letter-spacing:1px;line-height:1}
.brand-tag{font-family:"Open Sans",sans-serif;font-weight:600;font-size:7px;color:var(--brand);letter-spacing:1.5px;margin-top:3px}
.phone{left:578px;top:15px;display:flex;align-items:center;gap:3px;font-size:17px;color:var(--brand-dark)}
.main-nav{left:276px;top:56px;display:flex;gap:0}
.main-nav a{display:block;font-size:12px;color:var(--brand-dark);text-decoration:none;padding:0 15px;height:32px;line-height:16px}
.main-nav a.current{border-bottom:3px solid var(--brand);padding-left:12px;padding-right:12px}

/* hero */
.hero{left:0;top:88px;width:765px;height:307px;background:linear-gradient(90deg,#6f8fa6 0%,#c9d4d8 30%,#e4e6e2 55%,#9a8d80 75%,#5f5e62 100%)}
.hero-title{left:0;top:90px;width:765px;text-align:center;color:var(--white);font-family:"Ubuntu",sans-serif;font-weight:400;text-shadow:0 1px 4px rgba(0,0,0,.35)}
.hero-title .l1{display:block;font-size:28px;line-height:34px}
.hero-title .l2{display:block;font-size:36px;line-height:42px}
.dots{left:362px;top:292px;display:flex;gap:3px}
.dots span{width:9px;height:9px;border-radius:50%;background:#888}
.dots span.on{background:#111}

/* about & projects */
.section-title{font-size:21px;color:var(--ink)}
.copy{font-size:7.6px;line-height:14.3px;color:var(--muted)}
.about{left:52px;top:422px;width:332px}
.about .copy{margin-top:9px}
.about .copy+.copy{margin-top:7px}
.projects{left:411px;top:422px;width:305px}
.project-grid{display:flex;gap:14px;margin-top:12px}
.project{width:145px}
.project .thumb{width:145px;height:63px;border:1px solid #ddd}
.project h3{font-size:10.5px;font-weight:400;color:var(--ink);margin-top:9px}
.project p{font-size:7.3px;line-height:12.8px;color:var(--soft);margin-top:2px}

/* services */
.services{left:0;top:625px;width:765px;height:242px;background:linear-gradient(180deg,var(--band-top),var(--band-bottom))}
.services .section-title{position:absolute;left:51px;top:30px;color:var(--white)}
.service-grid{position:absolute;left:50px;top:65px;display:flex;gap:8px}
.service{width:160px}
.service .thumb{width:160px;height:74px;border:1px solid #fff}
.service h3{font-size:10.5px;font-weight:400;color:var(--white);margin:6px 0 0 2px}
.service p{font-size:7.5px;line-height:11.8px;color:#e6eef4;margin:3px 0 0 2px}

/* feature */
.feature{left:53px;top:898px;width:345px}
.feature h2{font-family:"Ubuntu",sans-serif;font-weight:300;font-size:24.5px;line-height:33px;color:var(--brand)}
.feature .copy{margin-top:10px}
.feature .copy+.copy{margin-top:7px}
.feature-art{left:402px;top:918px;width:312px;height:168px;border-radius:6px;background:radial-gradient(ellipse at center,#6fa7dc 0%,#bcd3e8 45%,#f4f6f8 80%)}

/* footer */
.site-footer{left:0;top:1118px;width:765px;height:82px;background:var(--footer)}
.footer-nav{position:absolute;left:57px;top:20px;display:flex;gap:20px}
.footer-nav a{font-size:11px;color:var(--ink);text-decoration:none}
.legal{position:absolute;left:57px;top:45px;font-size:8.5px;color:var(--soft)}
.social{position:absolute;left:616px;top:21px;display:flex;gap:2px}
.social span{width:22px;height:22px;border-radius:50%;background:#111}
</style>
</head>
<body>

<header class="site-header abs">
  <div class="brand abs">
    <span class="brand-dot"></span>
    <div>
      <div class="brand-name">novaleap</div>
      <div class="brand-tag">consulting that delivers</div>
    </div>
  </div>
  <div class="phone abs">
    <svg width="12" height="16" viewBox="0 0 12 16" aria-hidden="true"><path d="M3 1 L5 4 L4 6 Q5 9 7 11 L9 10 L11 13 L9 15 Q3 13 1 4 Z" fill="#c8c8c8"/></svg>
    <span>555.204.7731</span>
  </div>
  <nav class="main-nav abs">
    <a class="current" href="#">HOME</a>
    <a href="#">ABOUT US</a>
    <a href="#">SERVICES</a>
    <a href="#">PROJECTS</a>
    <a href="#">BLOG</a>
    <a href="#">CONTACT</a>
  </nav>
</header>

<section class="hero abs" role="img" aria-label="Photo of a smiling business team in a bright office">
  <h1 class="hero-title abs"><span class="l1">Specialize in Consulting and Advise on</span><span class="l2">Global Software Delivery</span></h1>
  <div class="dots abs"><span class="on"></span><span></span><span></span><span></span></div>
</section>

<section class="about abs">
  <h2 class="section-title heading">About Our Company</h2>
  <p class="copy">Aascetur ridiculus mus In iaculis facilisis massa Etiam eu urna Sed porta Suspendisse quam leo molestie sed luctus quis feugiat in pede Fusce tellus Sed metus augue convallis et vehicula ut pulvinar eu ante Integer orci tellus tristique vitae consequat nec porta vel lectus Nulla sit amet diam Duis non nunc libero a tempus libero lectus feugiat felis</p>
  <p class="copy">Phasellus felis dolor scelerisque a tempus eget lobortis id libero Aliquam nec erat at purus cursus interdum Vestibulum ligula augue bibendum accumsan vestibulum ut commodo a mi Morbi ornare gravida elit Integer congue augue et malesuada iaculis ipsum dui aliquet felis at cursus magna nisl nec elit Vestibulum gravida Praesent elementum elit at tellus Malesuada nec ultricies sit amet porttitor mattis enim In massa libero interdum nec interdum</p>
</section>

<section class="projects abs">
  <h2 class="section-title heading">Latest Projects</h2>
  <div class="project-grid">
    <article class="project">
      <div class="thumb" role="img" aria-label="Illustration of a blue globe linked to a network of nodes" style="background:linear-gradient(135deg,#f4f8fa,#a9d3e6 60%,#3b8fc6)"></div>
      <h3>Donec scelerisque leo</h3>
      <p>Class aptent taciti sociosqu ad litora torquent per conubia nostra, per incep-tos hymenaeos Proin nulla arcu.</p>
    </article>
    <article class="project">
      <div class="thumb" role="img" aria-label="Photo of a hand touching a digital world map" style="background:linear-gradient(135deg,#3a3a3e,#8f8f96 55%,#2c2c30)"></div>
      <h3>Donec scelerisque leo</h3>
      <p>Class aptent taciti sociosqu ad litora torquent per conubia nostra, per incep-tos hymenaeos Proin nulla arcu.</p>
    </article>
  </div>
</section>

<section class="services abs">
  <h2 class="section-title heading">Services We Provide</h2>
  <div class="service-grid">
    <article class="service">
      <div class="thumb" role="img" aria-label="Illustration of a central hub connected to surrounding nodes" style="background:linear-gradient(135deg,#fbfbfb,#e6eef4 60%,#c7d6e2)"></div>
      <h3>Project Tittle here</h3>
      <p>Mauris vel lacus vitae felis vestibulum volutpat. Etiam est nunc, venenatis in tristique imperdiet</p>
    </article>
    <article class="service">
      <div class="thumb" role="img" aria-label="Photo of a businesswoman with a tablet over a world map" style="background:linear-gradient(135deg,#8c8c8c,#d6d6d6 50%,#9a9a9a)"></div>
      <h3>Project Tittle here</h3>
      <p>Mauris vel lacus vitae felis vestibulum volutpat. Etiam est nunc, venenatis in tristique imperdiet</p>
    </article>
    <article class="service">
      <div class="thumb" role="img" aria-label="Photo of a businessman touching digital media icons" style="background:linear-gradient(135deg,#1a3ea8,#4d8ee0 55%,#2a2a33)"></div>
      <h3>Project Tittle here</h3>
      <p>Mauris vel lacus vitae felis vestibulum volutpat. Etiam est nunc, venenatis in tristique imperdiet</p>
    </article>
    <article class="service">
      <div class="thumb" role="img" aria-label="Illustration of server racks beside a globe" style="background:linear-gradient(90deg,#2b2b2f,#8a8d93 55%,#cfe3f2 80%,#3a86d0)"></div>
      <h3>Project Tittle here</h3>
      <p>Mauris vel lacus vitae felis vestibulum volutpat. Etiam est nunc, venenatis in tristique imperdiet</p>
    </article>
  </div>
</section>

<section class="feature abs">
  <h2>How to secure innovation within the Global delivery platform.</h2>
  <p class="copy">Aascetur ridiculus mus In iaculis facilisis massa Etiam eu urna Sed porta Suspendisse quam leo molestie sed luctus quis feugiat in pede Fusce tellus Sed metus augue convallis et vehicula ut pulvinar eu ante Integer orci tellus tristique vitae consequat nec porta vel lectus Nulla sit amet diam Duis non nunc libero a tempus libero lectus feugiat felis</p>
  <p class="copy">Etiam eu urna Sed porta Suspendisse quam leo molestie sed luctus quis feugiat in pede Fusce tellus Sed metus augue convallis et vehicula ut pulvinar eu ante Integer orci tellus tristique vitae consequat nec porta vel lectus Nulla sit amet diam Duis non nunc</p>
</section>
<div class="feature-art abs" role="img" aria-label="Illustration of two laptops linked by a globe"></div>

<footer class="site-footer abs">
  <nav class="footer-nav">
    <a href="#">HOME</a>
    <a href="#">ABOUT US</a>
    <a href="#">SERVICES</a>
    <a href="#">PROJECTS</a>
    <a href="#">BLOG</a>
    <a href="#">CONTACT</a>
  </nav>
  <p class="legal">© 2014 Company Name.&nbsp; All right reserved.&nbsp; Term of Use</p>
  <div class="social" aria-label="Social links"><span></span><span></span><span></span><span></span></div>
</footer>

</body>
</html>
```